Home Improvements Website

I would like a website that matches our business colour scheme and uses the fonts consistent without logo. (Monserrat, Chosence & Big Noddle Tiling).
We will need numerous sections: homepage, about us, services (with tiles or links to each service - building, landscaping, decking, maintenance, roofing, gutters etc) current projects (which must be easily editable by me, who is not too tech savvy) and a contacts page with enquiry form we can link to our job management service (Tradify).

```html
<!DOCTYPE html>
<html lang="en">
<head>
<meta charset="utf-8">
<title>Oakridge Home Improvements – Building &amp; Landscaping</title>
<link href="https://fonts.googleapis.com/css2?family=Montserrat:wght@400;500;600&family=Teko:wght@300;400;500&display=swap" rel="stylesheet">
<style>
:root{
  --green:#1aa31e;
  --green-light:#7cc63a;
  --green-dark:#0f7d14;
  --charcoal:#2f3532;
  --ink:#2a2d2b;
  --white:#ffffff;
  --line:#d9d9d9;
  --muted:#555;
}
*{box-sizing:border-box;margin:0;padding:0}
html,body{width:1200px;height:4141px;overflow:hidden}
body{position:relative;background:var(--white);font-family:"Montserrat",sans-serif;color:var(--ink)}

/* buttons */
.btn{position:absolute;z-index:2;isolation:isolate;height:52px;display:flex;align-items:center;justify-content:center;color:var(--white);font-family:"Teko",sans-serif;font-size:24px;letter-spacing:1px;text-transform:uppercase;text-decoration:none}
.btn::before{content:"";position:absolute;inset:0;background:var(--green);transform:skewX(-20deg);z-index:-1}
.btn::after{content:"";position:absolute;top:0;bottom:0;right:-14px;width:8px;background:var(--green-light);transform:skewX(-20deg)}
.btn span{position:relative;line-height:1;padding-top:4px}

/* header */
.header{position:absolute;top:0;left:0;width:1200px;height:92px;background:var(--white);z-index:5}
.brand{position:absolute;left:118px;top:0;width:152px;height:165px;background:var(--white);display:flex;align-items:center;justify-content:center;flex-direction:column;z-index:6;box-shadow:0 4px 10px rgba(0,0,0,.15)}
.brand-name{font-family:"Teko",sans-serif;font-size:40px;color:var(--charcoal);letter-spacing:2px;line-height:1}
.nav{position:absolute;left:318px;top:30px;display:flex}
.nav a{font-family:"Teko",sans-serif;font-size:22px;color:var(--ink);text-decoration:none;padding:0 29px;border-left:1px solid var(--line);line-height:30px;text-transform:uppercase}
.nav a:first-child{border-left:0;padding-left:0;position:relative}
.nav a.active::after{content:"";position:absolute;left:0;right:29px;bottom:-6px;height:3px;background:var(--green)}
.call{position:absolute;right:0;top:0;width:245px;height:92px;display:flex;align-items:center;justify-content:center;gap:12px;color:var(--white);font-family:"Teko",sans-serif;font-size:32px;isolation:isolate}
.call::before{content:"";position:absolute;inset:0 0 0 10px;background:var(--green);transform:skewX(-10deg);transform-origin:bottom;z-index:-1}
.call-icon{width:30px;height:30px;border-radius:50%;background:var(--white);display:flex;align-items:center;justify-content:center}

/* hero */
.hero{position:absolute;top:92px;left:0;width:1200px;height:648px;background:linear-gradient(180deg,#8fb2c9 0%,#b9ccd2 22%,#5e7b3f 45%,#4c8c2a 70%,#6aa43a 100%)}
.hero-eyebrow{position:absolute;left:106px;top:170px;color:var(--white);font-family:"Teko",sans-serif;font-size:30px;text-transform:uppercase}
.hero-eyebrow::before{content:"";position:absolute;left:-106px;top:16px;width:86px;height:1px;background:var(--white)}
.hero-title{position:absolute;left:104px;top:205px;color:var(--white);font-family:"Teko",sans-serif;font-size:112px;line-height:.86;letter-spacing:3px;text-transform:uppercase;font-weight:500}

/* section heads */
.section-head{position:absolute;left:0;width:1200px;text-align:center}
.eyebrow{font-family:"Teko",sans-serif;font-size:30px;color:var(--green);text-transform:uppercase;line-height:1}
.heading{font-family:"Teko",sans-serif;font-size:62px;color:var(--ink);text-transform:uppercase;line-height:1;letter-spacing:2px}
.rule{width:56px;height:3px;background:var(--green);margin:4px auto 0}

/* hex tiles */
.hex{position:absolute;width:250px;height:290px;clip-path:polygon(50% 0,100% 25%,100% 75%,50% 100%,0 75%,0 25%)}
.hex-label{position:absolute;left:0;right:0;bottom:54px;text-align:center;color:var(--white);font-family:"Teko",sans-serif;font-size:32px;text-transform:uppercase}
.hex-label::after{content:"";display:block;width:30px;height:3px;background:var(--green);margin:0 auto}
.hex.featured{background:var(--green);color:var(--white);text-align:center;padding:78px 34px 0}
.hex.featured h3{font-family:"Teko",sans-serif;font-weight:400;font-size:34px;line-height:1;text-transform:uppercase}
.hex.featured p{font-size:11.5px;line-height:1.45;margin-top:10px}
.hex.featured a{display:inline-block;margin-top:10px;color:var(--white);font-family:"Teko",sans-serif;font-size:19px;text-decoration:underline}

/* about */
.about{position:absolute;top:1590px;left:0;width:1200px;height:690px;background:var(--charcoal);clip-path:polygon(0 110px,50% 0,100% 110px,100% 100%,0 100%)}
.about-frame{position:absolute;left:140px;top:1688px;width:430px;height:506px;background:var(--white);clip-path:polygon(50% 0,100% 25%,100% 75%,50% 100%,0 75%,0 25%)}
.about-frame-inner{position:absolute;left:16px;top:16px;right:16px;bottom:16px;background:var(--charcoal);clip-path:polygon(50% 0,100% 25%,100% 75%,50% 100%,0 75%,0 25%)}
.about-photo{position:absolute;left:158px;top:1730px;width:394px;height:440px;background:linear-gradient(180deg,#cfe3f0 0%,#8aa290 40%,#5c9a3c 70%,#a8c85a 100%);clip-path:polygon(50% 0,100% 25%,100% 75%,50% 100%,0 75%,0 25%)}
.about-text{position:absolute;left:667px;top:1758px;width:440px;color:var(--white)}
.about-text .heading{color:var(--white);font-size:56px;line-height:.98;margin-top:4px}
.about-text .rule{margin:10px 0 0}
.about-text p{font-size:16px;line-height:1.7;margin-top:18px;color:#e8e8e8}

/* gallery */
.tile{position:absolute}

/* contact */
.contact{position:absolute;top:3130px;left:0;width:1200px;height:680px;background:linear-gradient(180deg,#1fa526 0%,#36ac2e 60%,#7cc63a 100%)}
.contact-info{position:absolute;left:118px;top:3255px;color:var(--white)}
.contact-info .eyebrow{color:var(--white);font-size:28px}
.contact-info .heading{color:var(--white);font-size:64px}
.contact-info .rule{margin:4px 0 0;background:var(--white)}
.contact-info p{font-size:18px;line-height:1.55;margin-top:20px;width:420px}
.info-row{display:flex;align-items:center;gap:12px;margin-top:22px}
.info-icon{width:44px;height:44px;border-radius:50%;background:var(--white);display:flex;align-items:center;justify-content:center;flex:none}
.info-row small{display:block;font-size:15px}
.info-row strong{display:block;font-size:18px;font-weight:600}
.quote{position:absolute;left:566px;top:3230px;width:537px;height:400px;background:var(--charcoal);border-radius:0 60px 0 60px;padding:44px 46px}
.quote h2{font-family:"Teko",sans-serif;font-weight:400;color:var(--white);font-size:38px;text-transform:uppercase;line-height:1}
.fields{display:grid;grid-template-columns:1fr 1fr;gap:12px 9px;margin-top:22px}
.field{background:var(--white);height:46px;font-size:12px;color:var(--muted);padding:14px 20px}
.field.wide{grid-column:1/3;height:92px}
.trees{position:absolute;left:0;top:3700px;width:1200px;height:110px}

/* footer */
.footer-nav{position:absolute;left:140px;top:3868px;width:950px;height:74px;border-top:1px solid var(--line);border-bottom:1px solid var(--line)}
.footer-nav a{position:absolute;top:24px;font-family:"Teko",sans-serif;font-size:24px;color:var(--ink);text-decoration:none;text-transform:uppercase}
.dot{position:absolute;top:35px;width:7px;height:7px;background:var(--green)}
.footer-brand{position:absolute;left:548px;top:3835px;width:128px;height:140px;background:var(--white);box-shadow:0 4px 10px rgba(0,0,0,.15);display:flex;align-items:center;justify-content:center}
.footer-contact{position:absolute;top:3995px;display:flex;align-items:center;gap:10px;font-size:14px}
.footer-contact small{display:block;color:var(--muted);font-size:14px}
.footer-contact strong{display:block;font-weight:600;font-size:15px}
.socials{position:absolute;left:866px;top:3998px;display:flex;gap:6px}
.socials span{width:35px;height:35px;border-radius:50%;background:var(--green)}
.copyright{position:absolute;left:0;top:4080px;width:1200px;text-align:center;font-size:12px;color:var(--muted)}
.copyright::before{content:"";position:absolute;left:140px;right:104px;top:-18px;height:1px;background:var(--line)}
.copyright a{color:var(--muted)}
</style>
</head>
<body>

<header class="header">
  <nav class="nav">
    <a class="active" href="#">Home</a>
    <a href="#">About Us</a>
    <a href="#">Services</a>
    <a href="#">Projects</a>
    <a href="#">Request a Free Quote</a>
  </nav>
  <div class="call">
    <span class="call-icon"><svg width="18" height="18" viewBox="0 0 24 24"><path fill="#1aa31e" d="M6.6 10.8a15.1 15.1 0 006.6 6.6l2.2-2.2c.3-.3.7-.4 1-.2 1.1.4 2.3.6 3.6.6.6 0 1 .4 1 1V20c0 .6-.4 1-1 1A17 17 0 013 4c0-.6.4-1 1-1h3.5c.6 0 1 .4 1 1 0 1.3.2 2.5.6 3.6.1.3 0 .7-.2 1z"/></svg></span>
    <span>0400 123 456</span>
  </div>
</header>
<div class="brand"><span class="brand-name">OAKRIDGE</span></div>

<section class="hero" role="img" aria-label="Photo of a landscaped backyard with lawn, stone path, garden beds and timber house">
  <div class="hero-eyebrow">Oakridge Home Improvements</div>
  <h1 class="hero-title">Building &amp;<br>Lanscpaing</h1>
  <a class="btn" href="#" style="left:112px;top:424px;width:154px;height:42px;font-size:20px"><span>Contact Us ›</span></a>
</section>

<div class="section-head" style="top:826px">
  <div class="eyebrow">What we do</div>
  <div class="heading" style="margin-top:8px">Services Provide</div>
  <div class="rule"></div>
</div>

<div class="hex" style="left:73px;top:943px;background:linear-gradient(180deg,#5e7d52,#8a5a32 55%,#3f6e2a)" role="img" aria-label="Photo of a timber cabin"><div class="hex-label">Building</div></div>
<div class="hex featured" style="left:335px;top:943px">
  <h3>Decking</h3>
  <p>Lorem ipsum dolor sit amet, consectetur adipiscing elit, sed do eiusmod tempor i</p>
  <a href="#">Learn More</a>
</div>
<div class="hex" style="left:597px;top:943px;background:linear-gradient(180deg,#3c6b2c,#6aa542 55%,#8f9a8c)" role="img" aria-label="Photo of a garden path with plants"><div class="hex-label">Landscaping</div></div>
<div class="hex" style="left:857px;top:943px;background:linear-gradient(180deg,#5a8a3a,#c4a27a 55%,#7c5a3a)" role="img" aria-label="Photo of a gardener tending plants"><div class="hex-label">Maintenance</div></div>
<div class="hex" style="left:201px;top:1166px;background:linear-gradient(180deg,#b89a6a,#5e5a55 55%,#7a7470)" role="img" aria-label="Photo of a nail gun on roof shingles"><div class="hex-label">Roofing</div></div>
<div class="hex" style="left:463px;top:1166px;background:linear-gradient(180deg,#9aa4a0,#3a3a38 50%,#c9a24a)" role="img" aria-label="Photo of a black gutter downpipe"><div class="hex-label">Gutters</div></div>
<div class="hex" style="left:725px;top:1166px;background:linear-gradient(180deg,#6a8a4a,#3f6a2a 55%,#2a3a2a)" role="img" aria-label="Photo of a lawn mower on grass"><div class="hex-label">Other</div></div>

<a class="btn" href="#" style="left:490px;top:1494px;width:200px"><span>Learn More ›</span></a>

<section class="about"></section>
<div class="about-frame"><div class="about-frame-inner"></div></div>
<div class="about-photo" role="img" aria-label="Photo of a stone house with landscaped front garden"></div>
<div class="about-text">
  <div class="eyebrow">Who we are</div>
  <div class="heading">About Oakridge<br>Home Improvement</div>
  <div class="rule"></div>
  <p>Lorem ipsum dolor sit amet, consectetur adipiscing elit, sed do eiusmod tempor incididunt ut labore et dolore magna aliqua. Quis ipsum suspendisse ultrices gravida. Risus commodo viverra maecenas accumsan lacus vel facilisis.</p>
</div>
<a class="btn" href="#" style="left:662px;top:2090px;width:200px"><span>Learn More ›</span></a>

<div class="section-head" style="top:2380px">
  <div class="eyebrow">Gallery</div>
  <div class="heading">Our Projects</div>
  <div class="rule"></div>
</div>

<div class="tile" style="left:104px;top:2505px;width:323px;height:230px;background:linear-gradient(180deg,#9cc0e0,#9a6a4a 45%,#5d9a3c)" role="img" aria-label="Project photo of brick homes and lawn"></div>
<div class="tile" style="left:439px;top:2505px;width:323px;height:230px;background:linear-gradient(180deg,#c8d6e0,#e8e8e6 35%,#8a4a3a 70%,#6a6a60)" role="img" aria-label="Project photo of a carport beside a brick house"></div>
<div class="tile" style="left:773px;top:2505px;width:323px;height:230px;background:linear-gradient(180deg,#8fb6e0,#d8d4c8 40%,#5a4a3a 60%,#6a8a3a)" role="img" aria-label="Project photo of a pergola over garden beds"></div>
<div class="tile" style="left:106px;top:2745px;width:491px;height:230px;background:linear-gradient(180deg,#7aa8d8,#e6dec8 35%,#8a7a60 70%,#6a6050)" role="img" aria-label="Project photo of a large outdoor shelter frame"></div>
<div class="tile" style="left:605px;top:2745px;width:492px;height:230px;background:linear-gradient(180deg,#a8c8e0,#3e7a2a 40%,#c86a8a 65%,#5aa33a)" role="img" aria-label="Project photo of a landscaped garden with flower beds"></div>

<a class="btn" href="#" style="left:500px;top:3010px;width:200px"><span>View More ›</span></a>

<section class="contact"></section>
<svg class="trees" viewBox="0 0 1200 110" preserveAspectRatio="none" aria-hidden="true"><path fill="#fff" d="M0 30 Q300 90 600 70 T1200 30 V110 H0Z"/></svg>
<div class="contact-info">
  <div class="eyebrow">Get in touch</div>
  <div class="heading">Contact Us</div>
  <div class="rule"></div>
  <p>Lorem ipsum dolor sit amet, consectetur adipiscing elit, sed do eiusmod</p>
  <div class="info-row">
    <span class="info-icon"><svg width="22" height="22" viewBox="0 0 24 24"><path fill="#1aa31e" d="M6.6 10.8a15.1 15.1 0 006.6 6.6l2.2-2.2c.3-.3.7-.4 1-.2 1.1.4 2.3.6 3.6.6.6 0 1 .4 1 1V20c0 .6-.4 1-1 1A17 17 0 013 4c0-.6.4-1 1-1h3.5c.6 0 1 .4 1 1 0 1.3.2 2.5.6 3.6.1.3 0 .7-.2 1z"/></svg></span>
    <div><small>Phone Number</small><strong>0400 123 456 / 0400 987 654</strong></div>
  </div>
  <div class="info-row">
    <span class="info-icon"><svg width="22" height="22" viewBox="0 0 24 24"><rect x="3" y="6" width="18" height="12" rx="1" fill="#1aa31e"/><path d="M3 7l9 6 9-6" stroke="#fff" stroke-width="1.6" fill="none"/></svg></span>
    <div><small>Email address</small><strong>info@oakridgehomes.example</strong></div>
  </div>
</div>

<form class="quote">
  <h2>Request a &nbsp;Free Quote</h2>
  <div class="fields">
    <div class="field">First Name*</div>
    <div class="field">Last Name*</div>
    <div class="field">Email address*</div>
    <div class="field">Phone*</div>
    <div class="field wide">Leave Message</div>
  </div>
</form>
<a class="btn" href="#" style="left:615px;top:3550px;width:150px;height:40px;font-size:20px"><span>Submit ›</span></a>

<nav class="footer-nav">
  <a href="#" style="left:8px">Home</a><span class="dot" style="left:100px"></span>
  <a href="#" style="left:143px">About Us</a><span class="dot" style="left:262px"></span>
  <a href="#" style="left:307px">Services</a>
  <a href="#" style="left:594px">Projects</a><span class="dot" style="left:710px"></span>
  <a href="#" style="left:760px">Request a Free Quote</a>
</nav>
<div class="footer-brand"><span class="brand-name" style="font-size:32px">OAKRIDGE</span></div>

<div class="footer-contact" style="left:137px">
  <span class="info-icon" style="background:var(--green);width:36px;height:36px"><svg width="18" height="18" viewBox="0 0 24 24"><path fill="#fff" d="M6.6 10.8a15.1 15.1 0 006.6 6.6l2.2-2.2c.3-.3.7-.4 1-.2 1.1.4 2.3.6 3.6.6.6 0 1 .4 1 1V20c0 .6-.4 1-1 1A17 17 0 013 4c0-.6.4-1 1-1h3.5c.6 0 1 .4 1 1 0 1.3.2 2.5.6 3.6.1.3 0 .7-.2 1z"/></svg></span>
  <div><small>Phone Number</small><strong>0400 123 456 / 0400 987 654</strong></div>
</div>
<div class="footer-contact" style="left:466px">
  <span class="info-icon" style="background:var(--green);width:36px;height:36px"><svg width="18" height="18" viewBox="0 0 24 24"><rect x="3" y="6" width="18" height="12" rx="1" fill="#fff"/><path d="M3 7l9 6 9-6" stroke="#1aa31e" stroke-width="1.6" fill="none"/></svg></span>
  <div><small>Email address</small><strong>info@oakridgehomes.example</strong></div>
</div>
<div class="socials" aria-label="Social links"><span></span><span></span><span></span><span></span><span></span></div>

<p class="copyright">Copyright © 2024 <a href="#">Oakridge Home Improvements.</a> All Right Reserved</p>

</body>
</html>
```